Lantern over the Harbor ~ A Widening Passage for Writers

My book is called “Lantern over the Harbor.” Its subtitle is “A Widening Passage for Writers.” It is a book about being a poet, writing poetry, and the ways in which poets are connected to both society and the central energy of the Universe. I want the cover design to be abstract and impressionistic. A suggestion of fireworks or a starburst would be a plus. To be consistent with the 3 other books I have published, I want the font for the title, as well as my name (Dorothea Quillbrake) to be Papyrus. The subtitle font can be something more plain and sans serif, like Arial or Franklin Gothic Book, probably in italics. As for color, I definitely want pale gold (angelic). Possible other complimentary colors could be either light or dark shades of gray, turquoise, rose, rust or red. I'm attaching the back cover text and also three pages from inside the book that have line drawings, to give an example of the interior artwork.
Updates

Forgot to mention: My book is a paperback. Its size will be 8.5" high and 5.5" wide. I'm self-publishing it, and it will be printed by Halvern Printworks in Nebraska, USA. It has 104 pages. I think you need the number of pages, in order to make the spine of the book the correct width.

Target Market(s)

My target market is people who write poetry or are interested in how poetry is written.

Industry/Entity Type

Poetry

Font styles to use
Sans Serif
Other font styles liked:
• Papyrus for the front cover. Arial or another sans serif font on the back cover.

Colors

Designer to choose colors to be used in the design.

Requirements
Must have
• My book cover needs to be inspiring and uplifting, as well as abstract and impressionistic, with kind of a "New Age" feel. I don't want anything that looks rigid and scholarly.
Nice to have
• The book talks about the connection poets have to the Universe and the Creative Energy at the center of everything. The cover should convey that Energy.
Should not have
• My cover should not be realistic, logical or straight-laced. I want something that feels free, imaginative and unfettered.

```html
<!DOCTYPE html>
<html lang="en">
<head>
<meta charset="utf-8">
<title>Lantern over the Harbor — Book Cover</title>
<link rel="stylesheet" href="https://fonts.googleapis.com/css2?family=Cinzel:wght@500;600&family=Open+Sans:ital,wght@1,500;1,600&display=swap">
<style>
  :root {
    --stone: #8a7f70;
    --pale-gold: #e2d19c;
    --gold: #c99a4a;
    --rust: #b4432f;
    --rose: #c9705a;
    --teal: #4f8a88;
    --deep-teal: #1f3b44;
    --sand: #c19b76;
    --cream: #f5eedf;
    --ivory: #fbf6ea;
    --title-font: Papyrus, "Cinzel", "Times New Roman", serif;
    --text-font: "Open Sans", "Franklin Gothic Book", Arial, sans-serif;
  }
  * { margin: 0; padding: 0; box-sizing: border-box; }
  html, body {
    width: 678px;
    height: 1200px;
    overflow: hidden;
    background: var(--deep-teal);
  }
  .cover {
    position: relative;
    width: 678px;
    height: 1200px;
    overflow: hidden;
  }
  .cover-art {
    position: absolute;
    inset: 0;
    background:
      radial-gradient(circle at 334px 546px, rgba(251,246,234,0.95) 0, rgba(236,214,160,0.85) 90px, rgba(212,168,90,0.55) 210px, rgba(212,168,90,0) 330px),
      radial-gradient(ellipse 260px 180px at 560px 40px, var(--pale-gold), rgba(226,209,156,0) 100%),
      radial-gradient(ellipse 300px 420px at 560px 300px, var(--rust), rgba(180,67,47,0) 100%),
      radial-gradient(ellipse 200px 240px at 620px 620px, var(--rose), rgba(201,112,90,0) 100%),
      radial-gradient(ellipse 220px 200px at 640px 1130px, var(--sand), rgba(193,155,118,0) 100%),
      radial-gradient(ellipse 420px 360px at 420px 850px, var(--teal), rgba(79,138,136,0) 100%),
      linear-gradient(180deg, var(--stone) 0%, #8c7f6d 38%, #5f7f7a 62%, var(--deep-teal) 85%, #18323a 100%);
  }
  .title-block {
    position: absolute;
    left: 0;
    right: 0;
    top: 912px;
    text-align: center;
    color: var(--cream);
    font-family: var(--title-font);
    font-weight: 600;
    text-shadow: 0 1px 3px rgba(10, 30, 35, 0.55);
  }
  .title-line {
    display: block;
    line-height: 1.1;
    white-space: nowrap;
  }
  .title-line--first { font-size: 38px; }
  .title-line--last { font-size: 42px; margin-top: 4px; }
  .subtitle {
    position: absolute;
    left: 0;
    right: 0;
    top: 1034px;
    text-align: center;
    font-family: var(--text-font);
    font-style: italic;
    font-weight: 500;
    font-size: 26px;
    color: var(--ivory);
    white-space: nowrap;
  }
  .author {
    position: absolute;
    left: 0;
    right: 0;
    top: 1080px;
    text-align: center;
    font-family: var(--title-font);
    font-weight: 600;
    font-size: 26px;
    color: var(--ivory);
    white-space: nowrap;
  }
</style>
</head>
<body>
  <main class="cover">
    <div class="cover-art" role="img" aria-label="Abstract painted background in stone grey, pale gold, rust red and turquoise with a radiant pale gold and ivory starburst bursting from the centre"></div>

    <h1 class="title-block">
      <span class="title-line title-line--first">LANTERN OVER THE</span>
      <span class="title-line title-line--last">HARBOR</span>
    </h1>

    <p class="subtitle">A Widening Passage for Writers</p>
    <p class="author">Dorothea Quillbrake</p>
  </main>
</body>
</html>
```